Masculine, visually appealing sales presentation for CPA firm

I have a basic power point that I use for sales presentations and I would like it to be updated to be more appealing and modern.

This is a presentation I give to real estate agents to help them close sales, save taxes, and resolve tax disputes. I would like the powerpoint to be updated to be more visually appealing. I have included the current powerpoint along with some of my logo files.

You don't have to use any of the pictures/clip art that is in the current power point. I only care that the words of the powerpoint make it to the new version.

Target Market(s)

Realtors, Real Estate Agents

Industry/Entity Type

Accounting

Requirements
Must have
• Visually appealing. I don't want it to look like I just took a template and made a normal powerpoint out of it. It should look custom.
Should not have
• Anything unprofessional, anything inconsistent with my brand

```html
<!DOCTYPE html>
<html lang="en">
<head>
<meta charset="utf-8">
<title>Taxation for Real Estate Professionals – Slide Deck</title>
<link href="https://fonts.googleapis.com/css2?family=Catamaran:wght@400;500;600;700;800&display=swap" rel="stylesheet">
<style>
:root{
  --teal:#35d3d6;
  --teal-deep:#22c3c7;
  --teal-soft:#8fdde0;
  --ink:#2f3336;
  --muted:#8a9095;
  --slide:#f5f6f7;
  --page:#ffffff;
}
*{margin:0;padding:0;box-sizing:border-box}
html,body{width:874px;height:1200px;overflow:hidden;background:var(--page)}
body{font-family:"Catamaran",sans-serif;color:var(--ink)}
.board{position:absolute;left:0;top:0;width:1100px;height:1510px;transform:scale(.7945);transform-origin:0 0}
.slide{position:absolute;width:500px;height:280px;background:var(--slide);overflow:hidden;box-shadow:0 2px 6px rgba(0,0,0,.18)}
.col-l{left:20px}.col-r{left:570px}
.row1{top:20px}.row2{top:311px}.row3{top:602px}.row4{top:893px}.row5{top:1184px}
.abs{position:absolute}
.footline{position:absolute;left:0;right:30px;top:269px;height:1px;background:var(--teal-soft)}
.pagenum{position:absolute;right:16px;top:264px;font-size:7px;font-weight:700;color:var(--teal-deep)}
.pill{position:absolute;left:50%;transform:translateX(-50%);top:34px;border:1px solid #b9c2c6;border-radius:3px;padding:1px 7px;font-size:11px;font-weight:800;color:var(--teal);letter-spacing:.3px;white-space:nowrap;background:#fff}
.item{position:absolute;width:150px}
.item .num{font-size:12px;font-weight:800;color:var(--teal);margin-right:4px}
.item .title{font-size:8px;font-weight:600;color:var(--ink)}
.item .desc{font-size:4.6px;line-height:1.35;color:var(--muted);padding-left:24px;width:135px}
.photo{position:absolute}
.quote{position:absolute;color:#fff;font-size:8.5px;line-height:1.3;text-align:center}
.qmark{font-size:20px;font-weight:800;line-height:1;color:#fff}
.plus{font-size:13px;font-weight:800;color:var(--ink);line-height:1}
.kicker{font-size:5px;color:var(--muted)}
.sec-title{font-size:12.5px;font-weight:800;line-height:1.1;color:var(--ink)}
.sec-title .hl{color:var(--teal)}
.body{font-size:5.6px;line-height:1.4;color:var(--muted)}
.brand{position:absolute;left:0;right:0;top:130px;text-align:center;font-size:34px;font-weight:800;color:var(--teal-deep);letter-spacing:.5px}
.tagline{position:absolute;left:0;right:0;top:173px;text-align:center;font-size:12px;color:var(--teal-deep)}
.society{position:absolute;left:0;right:0;top:264px;text-align:center;font-size:8px;color:var(--teal-soft)}
.intro-h{position:absolute;left:0;right:0;top:18px;text-align:center;font-size:27px;font-weight:800;color:var(--teal)}
.presented{position:absolute;left:115px;width:262px;top:52px;display:flex;align-items:center;gap:6px;font-size:14px;font-weight:500}
.presented::before,.presented::after{content:"";flex:1;height:1px;background:#7b86a8}
.bio-name{font-size:9px;font-weight:600}
.bio{font-size:5.8px;line-height:1.35;color:#555}
.toc{position:absolute;left:132px;top:133px;width:236px;height:30px;border:1px solid #b9c2c6;border-radius:4px;text-align:center;font-size:21px;font-weight:800;color:var(--teal);line-height:30px;background:#fff}
.perk{position:absolute;display:flex;align-items:flex-start;gap:12px;color:#fff;font-size:10.5px;line-height:1.3}
.ws{position:absolute;left:38px;top:56px;width:230px;color:#fff;font-size:13px}
.ws-row{display:flex;justify-content:space-between;height:23px;align-items:flex-end}
.ws-row .v{width:68px}
.ws-row .v.ul{border-bottom:2px solid #fff}
.ws-total{margin-top:4px;margin-left:-4px;width:226px;background:#fff;color:var(--ink);border-radius:2px;padding:0 4px;display:flex;justify-content:space-between;height:17px;align-items:center}
.ws-total .v{width:68px}
.note{position:absolute;left:208px;top:200px;width:100px;color:#fff;font-size:7px;font-weight:700;font-style:italic;line-height:1.3}
</style>
</head>
<body>
<div class="board">

  <section class="slide col-l row1">
    <div class="photo" style="inset:0;background:linear-gradient(100deg,#dfe6e8 0%,#f2f5f6 40%,#fbfcfc 70%,#e9eef0 100%)" role="img" aria-label="Bright empty office interior with glass walls"></div>
    <div class="brand">The Ledger CPA</div>
    <div class="tagline">Helping you to achieve your goals</div>
    <div class="society">National Guild of Tax Resolvers</div>
  </section>

  <section class="slide col-r row1">
    <div class="pill">TAXATION AND THE REALTOR</div>
    <div class="item" style="left:22px;top:76px"><span class="num">01.</span><span class="title">Estimated taxes</span><p class="desc">Key points for agents and their clients on this topic.</p></div>
    <div class="item" style="left:180px;top:76px"><span class="num">02.</span><span class="title">Tax areas of special interest</span><p class="desc">Key points for agents and their clients on this topic.</p></div>
    <div class="item" style="left:348px;top:76px"><span class="num">03.</span><span class="title">Home office</span><p class="desc">Key points for agents and their clients on this topic.</p></div>
    <div class="item" style="left:22px;top:136px"><span class="num">04.</span><span class="title">Automobile</span><p class="desc">Key points for agents and their clients on this topic.</p></div>
    <div class="item" style="left:180px;top:136px"><span class="num">05.</span><span class="title">Employ children</span><p class="desc">Key points for agents and their clients on this topic.</p></div>
    <div class="item" style="left:348px;top:136px"><span class="num">06.</span><span class="title">Employ adult family</span><p class="desc">Key points for agents and their clients on this topic.</p></div>
    <div class="item" style="left:22px;top:195px"><span class="num">07.</span><span class="title">Family employees</span><p class="desc">Key points for agents and their clients on this topic.</p></div>
    <div class="item" style="left:180px;top:195px"><span class="num">08.</span><span class="title">Accounting Systems</span><p class="desc">Key points for agents and their clients on this topic.</p></div>
    <div class="item" style="left:348px;top:195px"><span class="num">09.</span><span class="title">$$$$$$$$$$$$$$</span><p class="desc">Key points for agents and their clients on this topic.</p></div>
    <div class="footline"></div><div class="pagenum">01</div>
  </section>

  <section class="slide col-l row2">
    <h1 class="abs" style="left:30px;top:84px;font-size:27px;line-height:1.28;font-weight:800;color:var(--teal)">Taxation for Real<br>Estate Professionals</h1>
    <h2 class="abs" style="left:30px;top:164px;font-size:16px;font-weight:500">Your Creative Subtitle</h2>
    <p class="abs body" style="left:30px;top:188px;width:215px;color:#555">A practical guide to the taxes agents face, with clear steps to save money, close more sales and settle disputes with confidence.</p>
    <div class="footline"></div><div class="pagenum">01</div>
  </section>

  <section class="slide col-r row2">
    <div class="pill">TAX PROBLEM SOLUTIONS</div>
    <div class="item" style="left:78px;top:68px"><span class="num">01.</span><span class="title">Unfiled returns</span><p class="desc">Key points for agents and their clients on this topic.</p></div>
    <div class="item" style="left:280px;top:68px"><span class="num">02.</span><span class="title">Ostrich method</span><p class="desc">Key points for agents and their clients on this topic.</p></div>
    <div class="item" style="left:78px;top:119px"><span class="num">03.</span><span class="title">If you owe money</span><p class="desc">Key points for agents and their clients on this topic.</p></div>
    <div class="item" style="left:280px;top:119px"><span class="num">04.</span><span class="title">How about audits?</span><p class="desc">Key points for agents and their clients on this topic.</p></div>
    <div class="abs" style="left:0;top:165px;width:500px;height:87px;background:var(--teal)"></div>
    <div class="photo" style="left:0;top:165px;width:300px;height:87px;background:linear-gradient(90deg,#cfe9ec 0%,#a9dfe4 55%,rgba(53,211,214,.9) 100%)" role="img" aria-label="Magnifying glass over printed tax forms"></div>
    <div class="quote" style="left:315px;top:196px;width:140px"><span class="qmark abs" style="left:-22px;top:-8px">“</span>Lorem ipsum dolor sit amet, consectetur adipisic eiusmod tempor incididunt uti.<span class="qmark abs" style="right:-20px;top:20px">”</span></div>
    <div class="footline"></div><div class="pagenum">01</div>
  </section>

  <section class="slide col-l row3">
    <div class="intro-h">Introductions</div>
    <div class="presented">Presented By</div>
    <div class="photo" style="left:113px;top:103px;width:90px;height:86px;border-radius:50%;background:radial-gradient(circle at 50% 40%,#8a7a66,#3d4a3e 70%)" role="img" aria-label="Portrait of the presenter"></div>
    <div class="abs" style="left:217px;top:108px;width:172px">
      <p class="bio-name">Dale Turner, CPA</p>
      <p class="bio" style="margin-top:4px">I have been in the accounting business for over 12 years serving Tacoma, WA and Bend, OR. I specialize in helping entrepreneurs achieve their goals by turning the burden of accounting into a powerful tool to grow their business.</p>
    </div>
    <div class="abs" style="left:146px;top:212px;font-size:16px;font-weight:800;color:var(--teal)">“</div>
    <p class="abs" style="left:146px;top:230px;font-size:7.5px;color:#444">Don't be afraid to give up the good to go for the great.</p>
    <p class="abs" style="left:290px;top:245px;font-size:5px;color:#555">-J. D. Harlan</p>
    <div class="abs" style="left:338px;top:238px;font-size:16px;font-weight:800;color:var(--teal)">”</div>
    <div class="footline"></div><div class="pagenum">01</div>
  </section>

  <section class="slide col-r row3">
    <div class="photo" style="left:0;top:0;width:500px;height:280px;clip-path:polygon(330px 0,500px 0,500px 280px,165px 280px);background:linear-gradient(135deg,#ffffff 0%,#eef1f4 55%,#cfe1ee 100%)" role="img" aria-label="Businessman in shirt and tie holding blue letter blocks"></div>
    <div class="abs plus" style="left:46px;top:36px">+</div>
    <div class="abs kicker" style="left:46px;top:50px">Section One</div>
    <div class="abs sec-title" style="left:46px;top:58px"><span class="hl">TAXATION</span> AND CLIENT</div>
    <p class="abs body" style="left:46px;top:89px;width:138px">This section covers the rules that matter most to agents and their clients, with plain examples of how each one affects a sale, the tax owed and the steps to take next.</p>
    <div class="footline"></div><div class="pagenum">01</div>
  </section>

  <section class="slide col-l row4">
    <svg class="abs" style="left:226px;top:50px" width="48" height="50" viewBox="0 0 48 50" aria-hidden="true">
      <rect x="3" y="2" width="42" height="4" fill="#2f3336"/>
      <rect x="6" y="6" width="36" height="28" fill="#fff" stroke="#2f3336" stroke-width="2"/>
      <rect x="12" y="12" width="24" height="16" fill="#d9f6f7"/>
      <line x1="24" y1="34" x2="24" y2="44" stroke="#2f3336" stroke-width="1.5"/>
      <circle cx="24" cy="46" r="2.5" fill="none" stroke="#2f3336" stroke-width="1.5"/>
    </svg>
    <div class="toc">TABLE OF CONTENTS</div>
    <div class="footline"></div><div class="pagenum">01</div>
  </section>

  <section class="slide col-r row4">
    <div class="abs plus" style="left:22px;top:84px">+</div>
    <div class="abs kicker" style="left:22px;top:98px">01</div>
    <div class="abs sec-title" style="left:22px;top:108px;font-size:11px"><span class="hl">SALE OF</span><br>PRINCIPAL RESIDENCE</div>
    <p class="abs body" style="left:22px;top:140px;width:138px">This section covers the rules that matter most to agents and their clients, with plain examples of how each one affects a sale, the tax owed and the steps to take next.</p>
    <div class="photo" style="left:180px;top:0;width:320px;height:280px;background:linear-gradient(160deg,#3fd7da 0%,#35d3d6 55%,#5cdcdf 100%)" role="img" aria-label="Agent handing house keys to a buyer"></div>
    <div class="abs" style="left:176px;top:84px;width:8px;height:22px;background:#fff;border-radius:4px"></div>
    <div class="abs" style="left:176px;top:134px;width:8px;height:22px;background:#fff;border-radius:4px"></div>
    <div class="abs" style="left:176px;top:184px;width:8px;height:22px;background:#fff;border-radius:4px"></div>
    <div class="abs" style="left:180px;top:0;width:320px;height:280px">
      <div class="perk" style="top:86px;left:42px">
        <svg width="20" height="18" viewBox="0 0 20 18" fill="none" stroke="#fff" stroke-width="1.2"><path d="M2 9 10 2l8 7"/><path d="M4 8v9h12V8"/><rect x="8" y="11" width="4" height="6"/></svg>
        <span>Only one principal residence permitted.</span>
      </div>
      <div class="perk" style="top:131px;left:42px">
        <svg width="20" height="20" viewBox="0 0 20 20" fill="none" stroke="#fff" stroke-width="1.2"><circle cx="7" cy="7" r="4"/><circle cx="13" cy="7" r="4"/><circle cx="7" cy="13" r="4"/><circle cx="13" cy="13" r="4"/></svg>
        <span>Exclusion of $250K of gain, or $500K<br>for married persons filing jointly.</span>
      </div>
      <div class="perk" style="top:183px;left:42px">
        <svg width="20" height="18" viewBox="0 0 20 18" fill="none" stroke="#fff" stroke-width="1.2"><rect x="2" y="4" width="16" height="12" rx="1"/><path d="M4 4l9-3 1 3"/><rect x="12" y="8" width="6" height="4"/></svg>
        <span>Must have been taxpayer's principal<br>residence for 2 of the last 5 years.</span>
      </div>
    </div>
    <div class="abs" style="right:16px;top:264px;font-size:7px;font-weight:700;color:#fff">01</div>
  </section>

  <section class="slide col-l row5">
    <div class="pill">TAXATION AND CLIENT</div>
    <div class="item" style="left:22px;top:90px"><span class="num">01.</span><span class="title">Sale of principal residence</span><p class="desc">Key points for agents and their clients on this topic.</p></div>
    <div class="item" style="left:180px;top:90px"><span class="num">02.</span><span class="title">Federal tax lien on real estate</span><p class="desc">Key points for agents and their clients on this topic.</p></div>
    <div class="item" style="left:348px;top:90px"><span class="num">03.</span><span class="title">Cancellation of debt</span><p class="desc">Key points for agents and their clients on this topic.</p></div>
    <div class="abs" style="left:0;top:165px;width:500px;height:87px;background:var(--teal)"></div>
    <div class="photo" style="left:210px;top:165px;width:290px;height:87px;background:linear-gradient(90deg,rgba(53,211,214,.95) 0%,#b9e7ea 45%,#e4eef0 100%)" role="img" aria-label="Calculator on top of tax return forms"></div>
    <div class="quote" style="left:45px;top:196px;width:130px"><span class="qmark abs" style="left:-22px;top:-8px">“</span>Lorem ipsum dolor sit amet, consectetur adipisic eiusmod tempor incididunt uti.<span class="qmark abs" style="right:-16px;top:20px">”</span></div>
    <div class="footline"></div><div class="pagenum">01</div>
  </section>

  <section class="slide col-r row5">
    <div class="photo" style="left:0;top:0;width:322px;height:280px;background:linear-gradient(170deg,#45d9dc 0%,#35d3d6 60%,#52dadd 100%)" role="img" aria-label="Model house resting on banknotes"></div>
    <div class="ws">
      <div class="ws-row"><span>Selling price</span><span class="v">$200,000</span></div>
      <div class="ws-row"><span>Less: Balance of PMM</span><span class="v ul">$100,000</span></div>
      <div class="ws-row"><span>Excess cash</span><span class="v">$100,000</span></div>
      <div class="ws-row"><span>Current tax on sale</span><span class="v ul">$20,000</span></div>
      <div class="ws-total"><span>Cash to IRS</span><span class="v">$80,000</span></div>
    </div>
    <svg class="abs" style="left:255px;top:155px" width="30" height="40" viewBox="0 0 30 40" fill="none" stroke="#fff" stroke-width="1.2"><path d="M6 2c14 4 18 20 6 32"/><path d="M12 34l-1-6M12 34l6-2"/></svg>
    <p class="note">Apply to old tax liability, any excess would remain with taxpayer</p>
    <div class="abs plus" style="left:345px;top:84px">+</div>
    <div class="abs kicker" style="left:345px;top:98px">02.</div>
    <div class="abs sec-title" style="left:345px;top:108px;font-size:11px"><span class="hl">FEDERAL TAX LIEN</span><br>ON REAL ESTATE</div>
    <p class="abs body" style="left:345px;top:140px;width:138px">This section covers the rules that matter most to agents and their clients, with plain examples of how each one affects a sale, the tax owed and the steps to take next.</p>
    <div class="abs" style="left:330px;right:30px;top:269px;height:1px;background:var(--teal-soft)"></div>
    <div class="pagenum">01</div>
  </section>

</div>
</body>
</html>
```